Copper Finch Agency Website - Wordpress Web UPDATED BRIEF

FINAL LOGO UPLOADED - please look to this as reference for how we would like the site to look and feel.

We are a digital marketing agency - looking to have a new website built. We are looking for a simple one page feel of site that will allow us to grow it later. (Feel free to take some liberties with that if your imagination veers off) Must be very, playful, bold, sleek and easily integrate video. Wordpress only.

Overview:

Copper Finch is a creative constellation. We are built on what's great about the shared economy. With access to thousands of content creators, designers, technicians, writers, strategists and other creatives around the world, we are built differently than a traditional “brick and mortar” Marketing Agency. We provide the traditional services our clients have come to expect, without the “5X factor” of covering the overhead common in the old agency model. We believe even better work can be created in collaboration with our clients and by passing those savings back to them for their use. Our clients pay for our art, our work and our passion –not our furniture.

"Copper Finch, Let's Start Something"

Target Market(s)

companies looking for creative agency help, video production, creative consulting and coaching

Industry/Entity Type

Digital Marketing

Coding

Coded - Design and coding required

Number of Pages Required

1 page

Font styles to use
Sans Serif

Colors
3277b5
33a6d7
ec1f27

Requirements
Must have
• Wordpress design is a must. Looking for a one sheet homepage - with sections that are all on the main front page. We will have videos to embed, and should be able to have client logos and easy access to show a variety of our creative work.
• Please look to the logo for how we would like the site to feel.
• Please think "icon process flow" instead of blocks of text (which we used to have). Use the text to explain what the process flow should represent - don't actually copy paste the text but show it visually in icons.
Nice to have
• innovation around how we show video content. solid colors complementary to our palette and aesthetic.
Should not have
• Standard HTML coding

```html
<!DOCTYPE html>
<html lang="en">
<head>
<meta charset="utf-8">
<title>Copper Finch Agency</title>
<link href="https://fonts.googleapis.com/css2?family=Oswald:wght@300;400;500;700&display=swap" rel="stylesheet">
<style>
:root{
  --blue:#2d64ad;
  --blue-deep:#1d4f95;
  --blue-light:#3b7cc4;
  --red:#e3141f;
  --red-bright:#f02a33;
  --ink:#3a2a26;
  --grey:#6a6a6a;
  --white:#ffffff;
  --pale:#dcdcdc;
}
*{margin:0;padding:0;box-sizing:border-box}
html,body{width:1200px;height:3363px;overflow:hidden;background:var(--white)}
body{position:relative;font-family:'Oswald',sans-serif;color:var(--ink)}
.abs{position:absolute}
.center{text-align:center}

/* header */
.site-header{left:0;top:0;width:1200px;height:80px;background:var(--white);border-bottom:2px solid var(--blue)}
.main-nav{right:145px;top:28px;display:flex;gap:36px;font-size:16px;color:#333;letter-spacing:.2px}
.brand{left:143px;top:-35px;width:204px;height:200px;border-radius:50%;background:var(--white);display:flex;align-items:center;justify-content:center;padding-top:60px;gap:8px;z-index:5}
.brand-mark{width:22px;height:22px;border-radius:50%;background:var(--blue)}
.brand-name{font-weight:700;font-size:24px;color:var(--blue-deep)}

/* hero */
.hero{left:0;top:80px;width:1200px;height:588px;background:linear-gradient(120deg,#6b4a3a 0%,#a8826a 35%,#d9cfc4 60%,#b7a08a 100%)}
.hero-title{left:330px;top:150px;width:790px;color:var(--white);font-weight:700;font-size:78px;line-height:74px;text-shadow:0 2px 6px rgba(0,0,0,.35)}
.hero-arrow{top:305px}

/* feature circles */
.feature-chain{left:0;top:520px}
.feature{width:292px;color:var(--white)}
.feature h3{font-size:21px;font-weight:500;margin-top:8px}
.feature p{font-size:15px;font-weight:300;line-height:20px;margin-top:10px}
.feature .btn{display:inline-block;margin-top:22px;background:var(--white);border-radius:18px;padding:6px 18px;font-size:13px}

/* overview */
.overview-title{left:0;top:958px;width:1200px;font-size:48px;font-weight:700;color:var(--ink)}
.overview-text{left:215px;top:1043px;width:770px;font-size:13.5px;line-height:29.5px;color:var(--grey);font-weight:300}
.overview-quote{left:0;top:1210px;width:1200px;font-size:25px;color:var(--blue);font-weight:400}
.overview-word{left:1048px;top:1320px;transform-origin:0 0;transform:rotate(-90deg);font-size:96px;font-weight:700;color:#e3e3e3;letter-spacing:2px}

/* services */
.services{left:0;top:1437px;width:1200px;height:927px;background:var(--blue)}
.video-frame{left:209px;top:1305px;width:782px;height:360px;background:linear-gradient(180deg,#3e6c78 0%,#2e5661 60%,#3a3a3a 100%)}
.section-ghost{left:0;width:1200px;font-size:100px;font-weight:700;letter-spacing:2px}
.services-title{left:0;top:1742px;width:1200px;font-size:48px;font-weight:500;color:var(--white)}
.service{width:220px;color:var(--white)}
.service h4{font-size:20px;font-weight:500;margin-top:6px}
.service p{font-size:12.5px;line-height:22px;font-weight:300;margin-top:6px}
.mascot-circle{left:811px;top:2098px;width:390px;height:266px;overflow:hidden}

/* partners */
.partners{left:0;top:2364px;width:1200px;height:462px;background:linear-gradient(180deg,#fbfbfb,#f3f3f3)}
.partners-title{left:0;top:2447px;width:1200px;font-size:48px;font-weight:700;color:#111}
.partner{top:2575px;width:197px;height:76px;border:1px solid #bdbdbd;background:var(--white);display:flex;align-items:center;justify-content:center;font-size:20px;color:#555}
.view-more{left:512px;top:2695px;width:176px;height:50px;border-radius:25px;background:var(--blue);color:var(--white);font-size:18px;font-weight:500;display:flex;align-items:center;justify-content:center}

/* gallery */
.gallery{left:0;top:2826px;width:1200px;height:214px;display:flex;gap:3px}
.gallery-item{flex:1;height:214px}

/* footer */
.site-footer{left:0;top:3043px;width:1200px;height:320px;background:var(--red)}
.contact{width:240px;color:var(--white)}
.contact h5{font-size:17px;font-weight:500;margin-top:14px}
.contact p{font-size:13.5px;line-height:22px;font-weight:300;margin-top:6px}
.footer-rule{left:0;top:3295px;width:1200px;height:1px;background:rgba(255,255,255,.3)}
.copyright{left:145px;top:3320px;font-size:12px;color:var(--white);font-weight:300}
.social{top:3312px;width:40px;height:40px;border:1.5px solid var(--white);border-radius:50%}
</style>
</head>
<body>

<header class="site-header abs">
  <nav class="main-nav abs">
    <span>HOME</span><span>ABOUT US</span><span>SERVICES</span><span>REVIEWS</span><span>GALLERY</span><span>CONTACT US</span>
  </nav>
</header>

<section class="hero abs" role="img" aria-label="Photo of a young woman working on a laptop in a bright brick-walled loft"></section>
<div class="brand abs"><span class="brand-mark"></span><span class="brand-name">COPPER FINCH</span></div>
<h1 class="hero-title abs center">DIGITAL<br>MARKETING AGENCY</h1>
<svg class="hero-arrow abs" style="left:64px" width="32" height="60" viewBox="0 0 32 60"><path d="M28 4 4 30l24 26" fill="none" stroke="#fff" stroke-width="6"/></svg>
<svg class="hero-arrow abs" style="left:1104px" width="32" height="60" viewBox="0 0 32 60"><path d="M4 4l24 26L4 56" fill="none" stroke="#fff" stroke-width="6"/></svg>

<!-- feature circles -->
<svg class="feature-chain abs" width="1200" height="380" viewBox="0 520 1200 380">
  <defs>
    <linearGradient id="gBlue" x1="0" y1="0" x2="0" y2="1"><stop offset="0" stop-color="#3a7ac2"/><stop offset="1" stop-color="#1c4a8e"/></linearGradient>
    <linearGradient id="gRed" x1="0" y1="0" x2="0" y2="1"><stop offset="0" stop-color="#f02a33"/><stop offset="1" stop-color="#d10d18"/></linearGradient>
  </defs>
  <g fill="#2459a3"><circle cx="320" cy="705" r="178"/><circle cx="600" cy="705" r="178"/><circle cx="879" cy="705" r="178"/></g>
  <g fill="#fff"><circle cx="320" cy="705" r="166"/><circle cx="600" cy="705" r="166"/><circle cx="879" cy="705" r="166"/></g>
  <circle cx="320" cy="705" r="146" fill="url(#gBlue)"/>
  <circle cx="879" cy="705" r="146" fill="url(#gBlue)"/>
  <circle cx="600" cy="705" r="146" fill="url(#gRed)"/>
  <g fill="none" stroke="#fff" stroke-width="2.5">
    <circle cx="304" cy="618" r="22"/><path d="M320 634l20 20"/><path d="M304 604v14M304 624v3"/>
    <rect x="568" y="606" width="56" height="38"/><path d="M578 636l10-10 8 6 12-14"/><circle cx="615" cy="632" r="10"/><path d="M622 639l10 10"/>
    <path d="M879 645c-16 0-24-12-24-24s10-22 24-22 24 10 24 22-8 24-24 24z"/><path d="M870 645v10h18v-10M879 605v30M848 600l-8-6M910 600l8-6"/>
  </g>
</svg>
<div class="feature abs center" style="left:174px;top:686px"><h3>DISCOVERY</h3><p>We are passionate about creating<br>with you,not just for you.</p><span class="btn" style="color:var(--blue)">READ MORE</span></div>
<div class="feature abs center" style="left:454px;top:686px"><h3>STRATEGY</h3><p>Content is only as good as you<br>plan to deliver it.</p><span class="btn" style="color:var(--red)">READ MORE</span></div>
<div class="feature abs center" style="left:733px;top:686px"><h3>CREATIVE</h3><p>We are ready for our close up!<br>Are you?</p><span class="btn" style="color:var(--blue)">READ MORE</span></div>

<!-- overview -->
<div class="overview-word abs">OVERVIEW</div>
<h2 class="overview-title abs center">COMPANY OVERVIEW</h2>
<p class="overview-text abs center">Copper Finch is a creative constellation. We are built on what's great about the shared economy.With access to thousands of content creators, designers, technicians, writers, strategists and other creatives around the world, we are built differently than a traditional “brick and mortar” Marketing Agency. We provide the traditional services our clients have come to expect, without the “5X factor” of covering the overhead common in the old agency model. We believe even better work can be created in collaboration with our clients and by passing those savings back to them for their use. Our clients pay for our art, our work and our passion –not our furniture.</p>
<p class="overview-quote abs center">"Copper Finch, Let's Start Something"</p>

<section class="services abs"></section>
<svg class="abs" style="left:195px;top:1288px" width="810" height="44" viewBox="0 0 810 44" fill="none" stroke="#e3141f" stroke-width="3"><path d="M2 42V2h40M808 42V2h-40"/></svg>
<div class="video-frame abs" role="img" aria-label="Video still of a creative team sitting against a teal wall with laptops"></div>
<svg class="abs" style="left:561px;top:1446px" width="78" height="78" viewBox="0 0 78 78"><circle cx="39" cy="39" r="35" fill="rgba(0,0,0,.25)" stroke="#fff" stroke-width="4"/><path d="M31 24l24 15-24 15z" fill="#fff"/></svg>

<div class="section-ghost abs center" style="top:1700px;color:rgba(255,255,255,.1)">WHAT WE DO</div>
<h2 class="services-title abs center">WHAT WE DO</h2>

<svg class="abs" style="left:0;top:1850px" width="1200" height="330" viewBox="0 1850 1200 330" fill="none" stroke="#fff" stroke-width="2.5">
  <circle cx="224" cy="1880" r="22"/><path d="M240 1896l22 22M224 1868v12M224 1886v3"/>
  <path d="M446 1920v-14h10v14M462 1920v-22h10v22M478 1920v-30h10v30M494 1920v-40h10v40M440 1890l58-36"/><path d="M490 1854h8v8"/>
  <rect x="676" y="1858" width="56" height="62"/><path d="M676 1870h56M686 1882h18M686 1894h26M686 1906h20M712 1912l22-30"/>
  <rect x="938" y="1860" width="56" height="48"/><path d="M930 1914h72M954 1878h24M954 1890h24"/>
  <path d="M230 2142c-14 0-20-10-20-20s8-18 20-18 20 8 20 18-6 20-20 20zM222 2142v10h16v-10M230 2090v-10M200 2104l-8-8M260 2104l8-8M196 2124h-10M264 2124h10"/>
  <circle cx="477" cy="2124" r="34"/><circle cx="477" cy="2124" r="18"/><circle cx="477" cy="2118" r="6"/><path d="M466 2136c2-8 20-8 22 0"/>
  <path d="M685 2150l10-26 30-30 14-4-4 14-30 30zM690 2124h-12l-6 12M711 2145v12l-12 6"/><circle cx="724" cy="2108" r="5"/>
</svg>

<div class="service abs center" style="left:120px;top:1936px"><h4>DISVOVERY</h4><p>Lorem ipsum dolor sit amet,<br>consectetur adipiscing usmod tempor<br>incididunt ut labore et dolore</p></div>
<div class="service abs center" style="left:364px;top:1936px"><h4>STRATEGY</h4><p>Lorem ipsum dolor sit amet,<br>consectetur adipiscing usmod tempor<br>incididunt ut labore et dolore</p></div>
<div class="service abs center" style="left:597px;top:1936px"><h4>CONTENT</h4><p>Lorem ipsum dolor sit amet,<br>consectetur adipiscing usmod tempor<br>incididunt ut labore et dolore</p></div>
<div class="service abs center" style="left:854px;top:1936px"><h4>COACHING</h4><p>Lorem ipsum dolor sit amet,<br>consectetur adipiscing usmod tempor<br>incididunt ut labore et dolore</p></div>
<div class="service abs center" style="left:120px;top:2172px"><h4>CREATIVE</h4><p>Lorem ipsum dolor sit amet,<br>consectetur adipiscing usmod tempor<br>incididunt ut labore et dolore</p></div>
<div class="service abs center" style="left:367px;top:2172px"><h4>PAID MEDIA</h4><p>Lorem ipsum dolor sit amet,<br>consectetur adipiscing usmod tempor<br>incididunt ut labore et dolore</p></div>
<div class="service abs center" style="left:597px;top:2172px"><h4>PROJECT MANAGEMENT</h4><p>Lorem ipsum dolor sit amet,<br>consectetur adipiscing usmod tempor<br>incididunt ut labore et dolore</p></div>

<svg class="mascot-circle abs" viewBox="0 0 390 266" role="img" aria-label="Brand mascot character holding a lit match inside a circle">
  <circle cx="195" cy="200" r="190" fill="#1d4f95"/>
  <circle cx="195" cy="200" r="178" fill="#7fa3d4"/>
</svg>

<!-- partners -->
<section class="partners abs" role="img" aria-label="Soft faded photo of a smiling woman with envelope doodles"></section>
<div class="section-ghost abs center" style="top:2405px;color:rgba(0,0,0,.1)">PARTNERS</div>
<h2 class="partners-title abs center">PARTNERS</h2>
<div class="partner abs" style="left:197px">Maple Hollow</div>
<div class="partner abs" style="left:415px">Donec Dolor</div>
<div class="partner abs" style="left:631px">Big Dummy</div>
<div class="partner abs" style="left:849px">Happy Client</div>
<div class="view-more abs">VIEW MORE</div>

<!-- gallery -->
<div class="gallery abs">
  <div class="gallery-item" style="background:linear-gradient(135deg,#e8e6e2,#bfbab3)" role="img" aria-label="Tablet on a white brick wall surrounded by plan sketches"></div>
  <div class="gallery-item" style="background:linear-gradient(135deg,#3f7a83,#2a5b63)" role="img" aria-label="Team holding speech bubble cards against a teal wall"></div>
  <div class="gallery-item" style="background:linear-gradient(135deg,#a4553b,#6d3526)" role="img" aria-label="Friends holding share and media signs in front of a brick wall"></div>
  <div class="gallery-item" style="background:linear-gradient(135deg,#f1f1f1,#c9ccd2)" role="img" aria-label="Woman beside a wall of rocket and idea sketches"></div>
</div>

<!-- footer -->
<footer class="site-footer abs"></footer>
<svg class="abs" style="left:0;top:3088px" width="1200" height="80" viewBox="0 3088 1200 80" fill="none" stroke="#fff" stroke-width="3">
  <circle cx="202" cy="3129" r="36"/><path d="M192 3116c-2 8 8 22 18 24l5-6-7-5-4 3c-4-2-7-6-8-10l3-3-4-8z" fill="#fff" stroke="none"/>
  <circle cx="428" cy="3129" r="36"/><path d="M428 3146s-12-13-12-21a12 12 0 0 1 24 0c0 8-12 21-12 21z"/><circle cx="428" cy="3125" r="4"/>
  <circle cx="707" cy="3129" r="36" fill="#2d64ad"/><circle cx="707" cy="3129" r="12"/><path d="M707 3121v8h6"/>
  <circle cx="956" cy="3129" r="36"/><rect x="943" y="3120" width="26" height="18" fill="#fff" stroke="none"/><path d="M943 3120l13 10 13-10" stroke="#e3141f" stroke-width="2"/>
</svg>
<div class="contact abs center" style="left:82px;top:3172px"><h5>PHONE</h5><p>1 888 888 8888</p></div>
<div class="contact abs center" style="left:308px;top:3172px"><h5>ADDRESS</h5><p>223,Lorem ipsum dolor sit amet<br>consectetur</p></div>
<div class="contact abs center" style="left:587px;top:3172px"><h5>HOURS</h5><p>Wednesday - Fridays (4 to 10pm)<br>Weekends (11am to 9pm).</p></div>
<div class="contact abs center" style="left:836px;top:3172px"><h5>EMAIL</h5><p>hello@copperfinch.example</p></div>
<div class="footer-rule abs"></div>
<p class="copyright abs">Copyrights © 2019, Copper Finch. All rights reserved &nbsp;|&nbsp; Privacy Policy &nbsp;|&nbsp; Terms of use</p>
<span class="social abs" style="left:875px"></span>
<span class="social abs" style="left:922px"></span>
<span class="social abs" style="left:969px"></span>
<span class="social abs" style="left:1014px"></span>

</body>
</html>
```